Flyer for annual LUMEN SUMMIT 2020

I would like a church event flyer designed. The event is called "LUMEN SUMMIT 2020". I am looking for a professional, yet catchy design that uses our brand colors and logo creatively while communicating key information of the event effectively.

1. The logo is attached in two color formats. The designer has the choice to use them as he/she want.

2. The location of the event is: Talbot Community Center, 482 Wexley Street, Portland, ME 04107

3. Time and date of event. The designer can organize and format the date and time as he/she pleases.
Thursday December 31st @ 6:30PM
Friday January 1st @ 6:30PM
Saturday 2nd @ 6:30PM
Sunday 3rd @ 4:30PM

4. The topic of the event is "Deep Wells and Tall Cedars". The designer is free to use this phrase as he/she pleases to create a good composition.

5. Speaker: Prophet Marcus Obuya (2 pictures of the speaker to choose from are attached)

6. Contact information: contact@harborvine.org - Telephone number: 207 583 2194

7. I would also like the following three words on the flyer. These words describe the focus of the event: FIRE, REVIVAL, PROPHETIC

Target Market(s)

Young adults

Font styles to use
Sans Serif

Requirements
Must have
• Logo, speaker's picture
Should not have
• cross image, church image

```html
<!DOCTYPE html>
<html lang="en">
<head>
<meta charset="utf-8">
<title>Lumen Summit 2020 Flyer</title>
<link rel="stylesheet" href="https://fonts.googleapis.com/css2?family=Montserrat:wght@300;400;500;600;700;800&display=swap">
<style>
  :root {
    --orange: #f39322;
    --orange-soft: rgba(255, 228, 196, 0.55);
    --black: #0e0e0e;
    --navy: #03355c;
    --navy-dark: #0a3a66;
    --white: #ffffff;
    --rust: #c8532a;
    --font: "Montserrat", sans-serif;
  }
  * { margin: 0; padding: 0; box-sizing: border-box; }
  html, body { width: 1059px; height: 1200px; overflow: hidden; background: #fff; }
  .flyer {
    position: relative; width: 1059px; height: 1200px; overflow: hidden;
    background: var(--orange); font-family: var(--font); color: var(--white);
  }
  .flyer-shapes { position: absolute; inset: 0; }
  .focus-words {
    position: absolute; font-weight: 400; color: var(--orange-soft);
    letter-spacing: -5px; line-height: 1; filter: blur(3px); font-size: 82px;
  }
  .focus-fire { right: 48px; top: 40px; }
  .focus-revival { right: 86px; top: 117px; }
  .focus-prophetic { left: 245px; top: 192px; }
  .speaker-photo {
    position: absolute; left: 640px; top: 290px; width: 419px; height: 560px;
    background: linear-gradient(180deg, rgba(60,35,25,0) 0%, rgba(60,35,25,0.55) 25%, var(--rust) 60%, #b4481f 100%);
    border-radius: 200px 200px 0 0;
  }
  .topic {
    position: absolute; left: 34px; top: 40px; color: var(--navy);
    font-weight: 800; font-size: 40px; line-height: 0.95;
  }
  .topic .topic-and { display: block; font-weight: 300; font-size: 34px; }
  .event-title { position: absolute; left: 30px; top: 410px; line-height: 1; }
  .event-title .title-main { display: block; font-weight: 700; font-size: 106px; letter-spacing: 1px; }
  .event-title .title-sub { display: block; font-weight: 700; font-size: 68px; margin-top: 26px; letter-spacing: 1px; }
  .event-title .title-year { display: block; font-weight: 500; font-size: 76px; margin-top: 18px; }
  .venue { position: absolute; left: 38px; top: 712px; display: flex; gap: 20px; color: var(--orange); }
  .venue-pin { width: 40px; height: 60px; margin-top: 4px; }
  .venue-text { font-size: 21px; line-height: 1.35; font-weight: 400; }
  .venue-text strong { font-weight: 700; }
  .speaker-label {
    position: absolute; right: 0; top: 760px; width: 210px; text-align: right;
    padding-right: 38px; font-size: 30px; font-weight: 500;
    border-bottom: 2px solid var(--white); line-height: 1.1;
  }
  .speaker-name { position: absolute; left: 518px; top: 808px; font-size: 30px; font-weight: 700; }
  .schedule-icon { position: absolute; left: 530px; top: 868px; width: 54px; height: 54px; }
  .schedule-rule { position: absolute; left: 448px; top: 928px; width: 142px; height: 2px; background: var(--white); }
  .schedule { position: absolute; left: 530px; top: 944px; list-style: none; font-size: 21px; line-height: 33px; font-weight: 400; }
  .schedule strong { font-weight: 700; }
  .contact { position: absolute; left: 530px; top: 1094px; list-style: none; font-size: 19px; font-weight: 400; }
  .contact li { display: flex; align-items: center; gap: 12px; height: 36px; }
  .contact svg { width: 30px; height: 30px; }
  .brand { position: absolute; left: 38px; top: 1090px; display: flex; align-items: center; gap: 12px; }
  .brand-dot { width: 22px; height: 22px; border-radius: 50%; background: var(--orange); }
  .brand-name { color: var(--navy); font-weight: 600; font-size: 54px; letter-spacing: 1px; }
</style>
</head>
<body>
<main class="flyer">
  <svg class="flyer-shapes" viewBox="0 0 1059 1200" width="1059" height="1200" aria-hidden="true">
    <polygon points="0,140 1059,623 1059,1200 0,1200" fill="#0e0e0e"/>
    <polygon points="0,917 443,1123 443,1200 0,1200" fill="#ffffff"/>
  </svg>

  <div class="focus-words focus-fire">FIRE</div>
  <div class="focus-words focus-revival">REVIVAL</div>
  <div class="focus-words focus-prophetic">PROPHETIC</div>

  <div class="speaker-photo" role="img" aria-label="Portrait of the speaker, Prophet Marcus Obuya, in an orange jacket"></div>

  <svg class="flyer-shapes" viewBox="0 0 1059 1200" width="1059" height="1200" aria-hidden="true">
    <path d="M448,1200 L453,847 Q455,806 500,790 L1059,657 L1059,1200 Z" fill="#03355c"/>
    <path d="M472,1200 L472,832 Q474,800 515,786 L1059,625" fill="none" stroke="#f39322" stroke-width="4"/>
  </svg>

  <h2 class="topic">DEEP WELLS<span class="topic-and">AND</span>TALL CEDARS</h2>

  <h1 class="event-title">
    <span class="title-main">LUMEN</span>
    <span class="title-sub">SUMMIT</span>
    <span class="title-year">2020</span>
  </h1>

  <div class="venue">
    <svg class="venue-pin" viewBox="0 0 40 60"><path d="M20 57 C 8 40 3 32 3 21 A17 17 0 0 1 37 21 C37 32 32 40 20 57 Z" fill="none" stroke="#f39322" stroke-width="2.5"/><circle cx="20" cy="21" r="7" fill="none" stroke="#f39322" stroke-width="2.5"/></svg>
    <p class="venue-text"><strong>TALBOT COMMUNITY CENTER,</strong><br>482 WEXLEY STREET, PORTLAND<br>&nbsp;ME 04107</p>
  </div>

  <div class="speaker-label">SPEAKER</div>
  <div class="speaker-name">PROPHET MARCUS OBUYA</div>

  <svg class="schedule-icon" viewBox="0 0 54 54" aria-hidden="true">
    <rect x="6" y="10" width="42" height="40" rx="4" fill="none" stroke="#fff" stroke-width="3"/>
    <line x1="6" y1="20" x2="48" y2="20" stroke="#fff" stroke-width="3"/>
    <line x1="16" y1="5" x2="16" y2="14" stroke="#fff" stroke-width="3"/>
    <line x1="38" y1="5" x2="38" y2="14" stroke="#fff" stroke-width="3"/>
    <g fill="#fff"><rect x="13" y="28" width="5" height="4"/><rect x="22" y="28" width="5" height="4"/><rect x="31" y="28" width="5" height="4"/><rect x="13" y="37" width="5" height="4"/><rect x="22" y="37" width="5" height="4"/><rect x="31" y="37" width="5" height="4"/></g>
  </svg>
  <div class="schedule-rule"></div>
  <ul class="schedule">
    <li><strong>THURSDAY</strong> DECEMBER 31ST @ 6:30PM</li>
    <li><strong>FRIDAY</strong> JANUARY 1ST @ 6:30PM</li>
    <li><strong>SATURDAY</strong> JANUARY 2ND @ 6:30PM</li>
    <li><strong>SUNDAY</strong> JANUARY 3RD @ 4:30PM</li>
  </ul>

  <ul class="contact">
    <li><svg viewBox="0 0 30 30" aria-hidden="true"><path d="M7 4 L11 4 L13 10 L10 12 Q12 18 18 20 L20 17 L26 19 L26 23 Q25 27 20 26 Q6 22 4 9 Q4 5 7 4 Z" fill="none" stroke="#b9c9c9" stroke-width="2"/></svg>207 583 2194</li>
    <li><svg viewBox="0 0 30 30" aria-hidden="true"><circle cx="15" cy="15" r="14" fill="#b9c9c9"/><text x="15" y="21" font-family="Montserrat, sans-serif" font-size="17" font-weight="700" fill="#03355c" text-anchor="middle">@</text></svg>CONTACT@HARBORVINE.ORG</li>
  </ul>

  <div class="brand">
    <span class="brand-dot"></span>
    <span class="brand-name">ORVEN</span>
  </div>
</main>
</body>
</html>
```